Stationary design for new high end strategy and business consulting company

We need a stationary design (incorporating business card, letter head, consultant profile, envelope, invoice etc.) for a new company called VANTORA that is based in Australia.

Company provides high end strategy consulting/ advisory services - business insight - to the professional services, financial services, legal and health industries - in the areas of:
- strategy
- business transformation
- performance and profitability improvement
- commercial negotiation and procurement.

to enable companies to deliver an exceptional client experience for minimum cost, differentiate themselves in the market and maximize profitability

Design needs to be simple, stylish and sophisticated, bold and engaging. It should convey growth and prosperity; intelligent insight into how to make a company better and be more profitable; unique business insight.

Business cards should feature VANTORA prominently as well as our Director’s name “Marisol Pettigrew”

Other contact details are as follows:
Mob: 0472 618 304
Email: mapettigrew@vantorahq.com
Web: www.vantorahq.com

Colour pallet should incorporate lime green, dark greys, silver/ white

Target Market(s)

Law Firms
Banks, Investment Banks and Financial Services Companies
Healthcare companies that own hospitals, nursing homes, radiology and pathology services

Industry/Entity Type

Financial

Font styles to use
Sans Serif

Colors
add136
5c5c5c
e9e9e9

```html
<!DOCTYPE html>
<html lang="en">
<head>
<meta charset="utf-8">
<title>VANTORA — Stationery Suite</title>
<link rel="stylesheet" href="https://fonts.googleapis.com/css2?family=Questrial&display=swap">
<style>
  :root {
    --lime: #9cc435;
    --lime-soft: #cfdfa2;
    --lime-pale: #dfe9c0;
    --charcoal: #333333;
    --grey: #5c5c5c;
    --silver: #e9e9e9;
    --paper: #ffffff;
    --ground: #f0f0f0;
  }
  * { box-sizing: border-box; margin: 0; padding: 0; }
  html, body { width: 1200px; height: 795px; overflow: hidden; }
  body {
    background: var(--ground);
    font-family: "Questrial", "Helvetica Neue", Arial, sans-serif;
    color: var(--charcoal);
    position: relative;
  }
  .item { position: absolute; overflow: hidden; }

  /* brand wordmark */
  .brand { display: flex; align-items: center; gap: 6px; }
  .brand-square { background: var(--charcoal); flex: none; }
  .brand-name { color: var(--charcoal); letter-spacing: 0.12em; line-height: 1; }

  .pattern-fill {
    position: absolute;
    background: linear-gradient(160deg, rgba(156,196,53,0) 0%, rgba(156,196,53,0.55) 55%, var(--lime) 100%);
  }

  /* letterhead */
  .letterhead { left: 298px; top: 38px; width: 275px; height: 370px; background: var(--paper); }
  .letterhead .header-band {
    position: absolute; left: 0; top: 0; width: 100%; height: 44px;
    background: linear-gradient(173deg, var(--paper) 0%, var(--paper) 55%, var(--lime-pale) 56%, var(--lime-soft) 100%);
  }
  .letterhead .header-pattern { left: 120px; top: 4px; width: 155px; height: 36px; }
  .letterhead .brand { position: absolute; left: 20px; top: 14px; }
  .letterhead .brand-square { width: 12px; height: 12px; }
  .letterhead .brand-name { font-size: 11px; }
  .letter-body {
    position: absolute; left: 22px; top: 72px; width: 232px;
    font-size: 5.4px; line-height: 8.1px; letter-spacing: 0.08em; color: var(--grey);
  }
  .letter-body p { margin-bottom: 7px; }
  .letter-footer {
    position: absolute; left: 0; bottom: 20px; width: 100%; text-align: center;
    font-size: 5.4px; line-height: 8px; letter-spacing: 0.1em;
  }
  .letterhead .base-band { position: absolute; left: 0; bottom: 0; width: 100%; height: 10px; background: var(--lime); }

  /* folder */
  .folder { left: 597px; top: 38px; width: 306px; height: 382px; background: var(--lime-soft); }
  .folder .brand { position: absolute; left: 15px; top: 22px; }
  .folder .brand-square { width: 26px; height: 26px; }
  .folder .brand-name { font-size: 19px; }
  .folder .folder-pattern { left: 100px; top: 10px; width: 206px; height: 372px; }

  /* business cards */
  .card { top: 435px; width: 120px; height: 65px; background: var(--lime-soft); }
  .card-front { left: 295px; }
  .card-front .white-panel { position: absolute; right: 0; top: 0; width: 32px; height: 100%; background: var(--paper); }
  .card-front .card-pattern { right: 0; top: 0; width: 40px; height: 65px; }
  .card-front .brand { position: absolute; left: 10px; top: 12px; gap: 4px; }
  .card-front .brand-square { width: 9px; height: 9px; }
  .card-front .brand-name { font-size: 8px; }
  .card-front .role { position: absolute; left: 0; width: 88px; top: 39px; text-align: center; font-size: 5.6px; letter-spacing: 0.22em; line-height: 9px; }
  .card-back { left: 453px; }
  .card-back .card-pattern { left: 0; top: 0; width: 30px; height: 40px; }
  .card-back .details {
    position: absolute; left: 0; top: 7px; width: 100%; text-align: center;
    font-size: 4.3px; line-height: 7.2px; letter-spacing: 0.1em;
  }
  .card-back .details .company { font-size: 6px; line-height: 9px; letter-spacing: 0.15em; }

  /* envelope back */
  .envelope-back { left: 612px; top: 447px; width: 288px; height: 143px; background: var(--paper); }
  .envelope-back .flap { position: absolute; left: 0; top: 0; width: 100%; height: 48px; background: var(--lime-soft); clip-path: polygon(0 0, 100% 0, 97% 100%, 3% 100%); }
  .envelope-back .side-bar { position: absolute; top: 52px; width: 6px; height: 91px; }
  .envelope-back .bar-left { left: 0; background: linear-gradient(var(--charcoal) 0 40%, var(--lime) 40% 100%); }
  .envelope-back .bar-right { right: 0; background: linear-gradient(var(--charcoal) 0 40%, var(--lime) 40% 100%); }

  /* envelope front */
  .envelope-front { left: 612px; top: 612px; width: 293px; height: 150px; background: var(--lime-soft); }
  .envelope-front .white-panel { position: absolute; right: 0; top: 0; width: 90px; height: 100%; background: var(--paper); }
  .envelope-front .env-pattern { right: 0; top: 0; width: 92px; height: 150px; }
  .envelope-front .bar-left { position: absolute; left: 0; top: 28px; width: 6px; height: 122px; background: linear-gradient(var(--charcoal) 0 45%, var(--lime) 45% 100%); }
  .envelope-front .brand { position: absolute; left: 18px; top: 12px; }
  .envelope-front .brand-square { width: 13px; height: 13px; }
  .envelope-front .brand-name { font-size: 10px; }
  .envelope-front .window { position: absolute; left: 128px; top: 48px; width: 150px; height: 48px; background: var(--lime); border-radius: 4px; border: 1px solid #8ab02b; }
  .envelope-front .address { position: absolute; left: 18px; top: 108px; font-size: 5.4px; line-height: 7.4px; letter-spacing: 0.12em; }

  /* notebook */
  .notebook { left: 295px; top: 565px; width: 133px; height: 197px; background: var(--lime-soft); }
  .notebook .top-panel { position: absolute; left: 0; top: 0; width: 100%; height: 53px; background: var(--paper); }
  .notebook .brand { position: absolute; left: 14px; top: 20px; }
  .notebook .brand-square { width: 16px; height: 16px; }
  .notebook .brand-name { font-size: 11px; }
  .notebook .note-pattern { left: 10px; top: 55px; width: 70px; height: 140px; }
  .notebook .edge-bar { position: absolute; right: 0; top: 0; width: 8px; height: 100%; background: linear-gradient(var(--lime) 0 35%, var(--charcoal) 35% 62%, var(--lime) 62% 100%); }
  .notebook .spine { position: absolute; left: 0; top: 0; width: 6px; height: 100%; background: repeating-linear-gradient(var(--grey) 0 2px, transparent 2px 6px); }

  /* key tag */
  .key-tag { left: 467px; top: 585px; width: 33px; height: 75px; background: var(--lime-soft); border: 2px solid var(--paper); border-radius: 4px; }
  .key-tag .brand { position: absolute; left: 0; width: 100%; top: 52px; justify-content: center; gap: 2px; }
  .key-tag .brand-square { width: 4px; height: 4px; }
  .key-tag .brand-name { font-size: 4.6px; letter-spacing: 0.06em; }

  /* eraser */
  .eraser { left: 480px; top: 685px; width: 25px; height: 77px; background: var(--paper); }
  .eraser .sleeve { position: absolute; left: 0; top: 0; width: 100%; height: 62px; background: var(--lime-pale); }
  .eraser .vertical-name {
    position: absolute; left: 8px; top: 12px; writing-mode: vertical-rl;
    font-size: 6.5px; letter-spacing: 0.12em; color: var(--charcoal);
  }
</style>
</head>
<body>

  <!-- Letterhead -->
  <section class="item letterhead">
    <div class="header-band"></div>
    <div class="pattern-fill header-pattern" role="img" aria-label="Scattered lime green square pattern"></div>
    <div class="brand"><span class="brand-square"></span><span class="brand-name">VANTORA</span></div>
    <div class="letter-body">
      <p>Mr. XYZ,<br>ABC Company,<br>Australia</p>
      <p>Thank you for meeting with our team last week. We have reviewed your current operating model and prepared a short set of findings for your board. Our work focuses on strategy, business transformation and the steady growth of profit across each of your service lines.</p>
      <p>In the coming weeks we will hold three working sessions with your leaders to test the options, agree on priorities and shape a clear plan. Each session will run for half a day and will draw on data from your finance, client and people teams. We will share a summary after every session so that progress stays visible and decisions can be made with confidence.</p>
      <p>We also propose a review of your supplier contracts, where we believe there is room to improve terms and reduce cost without harm to service quality. Our negotiation team has led similar reviews for banks, law firms and hospital groups across the country.</p>
      <p>Please let us know a suitable date to begin. We look forward to working with you.</p>
      <p>Name here<br>CEO</p>
    </div>
    <div class="letter-footer">XYZ street, City :ABC, Australiya - 09876, 0472 618 304<br>www.vantorahq.com</div>
    <div class="base-band"></div>
  </section>

  <!-- Presentation folder -->
  <section class="item folder">
    <div class="pattern-fill folder-pattern" role="img" aria-label="Rising trail of lime green squares"></div>
    <div class="brand"><span class="brand-square"></span><span class="brand-name">VANTORA</span></div>
  </section>

  <!-- Business card front -->
  <section class="item card card-front">
    <div class="white-panel"></div>
    <div class="pattern-fill card-pattern" role="img" aria-label="Lime green square pattern"></div>
    <div class="brand"><span class="brand-square"></span><span class="brand-name">VANTORA</span></div>
    <div class="role">DIRECTOR<br>MARISOL PETTIGREW</div>
  </section>

  <!-- Business card back -->
  <section class="item card card-back">
    <div class="pattern-fill card-pattern" role="img" aria-label="Lime green square pattern"></div>
    <div class="details">
      <div class="company">VANTORA inc.</div>
      XYZ street,City :ABC,<br>
      Australiya - 09876<br>
      Mob: 0472 618 304<br>
      Email: mapettigrew@vantorahq.com<br>
      Web: www.vantorahq.com
    </div>
  </section>

  <!-- Envelope back -->
  <section class="item envelope-back">
    <div class="flap"></div>
    <div class="side-bar bar-left"></div>
    <div class="side-bar bar-right"></div>
  </section>

  <!-- Envelope front -->
  <section class="item envelope-front">
    <div class="white-panel"></div>
    <div class="pattern-fill env-pattern" role="img" aria-label="Lime green square pattern"></div>
    <div class="bar-left"></div>
    <div class="brand"><span class="brand-square"></span><span class="brand-name">VANTORA</span></div>
    <div class="window"></div>
    <div class="address">XYZ street,<br>City :ABC,<br>Australiya - 09876<br>0472 618 304<br>www.vantorahq.com</div>
  </section>

  <!-- Notebook cover -->
  <section class="item notebook">
    <div class="top-panel"></div>
    <div class="spine"></div>
    <div class="brand"><span class="brand-square"></span><span class="brand-name">VANTORA</span></div>
    <div class="pattern-fill note-pattern" role="img" aria-label="Scattered lime green square pattern"></div>
    <div class="edge-bar"></div>
  </section>

  <!-- Key tag -->
  <section class="item key-tag">
    <div class="brand"><span class="brand-square"></span><span class="brand-name">VANTORA</span></div>
  </section>

  <!-- Eraser sleeve -->
  <section class="item eraser">
    <div class="sleeve"></div>
    <span class="vertical-name">VANTORA</span>
  </section>

</body>
</html>
```